VornaDerm/The experts in permanent hairremoval

Our Brand is VornaDerm and we are specialized on permantent hair removal for the body for men and woman. VornaDerm is working as a Franchise chain.
The brand should be positioned as lifestyle brand but with a medical background. People should trust in us. We take care about their body. This need to be communicated 100%.
Our system is inexpensive but we don't want to show that we are cheap. So we want to communicate that permanent hair removal is a real lifestyle product but affordable.
We already created a logo that you can see the style and colour we prefer.

Target Market(s)

Europe beginning (especially german spoken markets), Middle East, Africa

Industry/Entity Type

Hair Removal

Number of Pages Required

5+ page

Font styles to use
Serif
Other font styles liked:
• Trajan Pro

Requirements
Nice to have
• We are very open for new ideas

```html
<!DOCTYPE html>
<html lang="en">
<head>
<meta charset="utf-8">
<title>VornaDerm – The Experts in Permanent Hair Removal</title>
<link rel="stylesheet" href="https://fonts.googleapis.com/css2?family=Cinzel:wght@400;700&family=Montserrat:wght@400;500;600;700&display=swap">
<style>
:root{
  --blue:#4aa8e0;
  --blue-dark:#2f8fcb;
  --grey:#77777a;
  --text:#555;
  --light:#f3f3f3;
  --footer:#333;
  --white:#fff;
}
*{box-sizing:border-box;margin:0;padding:0}
html,body{width:1200px;height:3163px;overflow:hidden;background:var(--white)}
body{position:relative;font-family:'Montserrat',sans-serif;color:var(--text)}
h2{font-weight:400}
.abs{position:absolute}
.serif{font-family:'Cinzel',serif}
.full{left:0;width:1200px;text-align:center}

/* header */
.brand{left:78px;top:22px;display:flex;align-items:center;gap:12px}
.brand-dot{width:46px;height:46px;border-radius:50%;background:var(--blue)}
.brand-name{font-family:'Montserrat',sans-serif;font-size:40px;font-weight:500;color:var(--grey);line-height:1}
.brand-tag{font-size:9.5px;color:var(--grey);letter-spacing:.3px;margin-top:5px}
.nav{top:0;left:474px;display:flex;align-items:flex-start}
.nav a{font-size:14px;color:#666;text-decoration:none;padding:46px 0 0;margin-right:31px;height:97px}
.nav a.active{background:var(--blue);color:var(--white);width:85px;text-align:center;margin-right:40px;
  clip-path:polygon(0 0,100% 0,100% 100%,50% 88%,0 100%)}

/* hero */
.hero{top:97px;left:0;width:1200px;height:559px;background:#fff}
.hero-man{left:0;top:97px;width:358px;height:559px;background:linear-gradient(180deg,#e9cdb9,#d9b29a)}
.hero-woman{left:496px;top:97px;width:704px;height:559px;background:linear-gradient(90deg,#fff 0%,#f1e4dc 35%,#e8d2c4 70%,#f7f3f0 100%)}
.hero-copy{left:300px;width:600px;top:262px;text-align:center}
.hero-kicker{font-size:22px;letter-spacing:2px;color:#444}
.hero-title{font-size:40px;font-weight:600;color:var(--blue);margin:8px 0 10px}
.hero-sub{font-size:22px;letter-spacing:1.5px;color:#444}
.dots{left:570px;top:447px;display:flex;gap:4px}
.dots span{width:16px;height:16px;border-radius:50%;background:#666}
.dots span:first-child{background:var(--white);border:3px solid var(--blue)}

/* why */
.why{top:656px;left:0;width:1200px;height:415px;background:var(--light)}
.why-mark{left:563px;top:716px;width:74px;height:74px;border-radius:50%;background:var(--blue)}
.why-title{top:868px;font-size:42px;color:var(--blue);letter-spacing:2px}
.why-text{top:938px;left:200px;width:800px;font-size:15.5px;line-height:28px;color:#666;text-align:center}

/* appointment */
.appoint{top:1071px;left:0;width:1200px;height:315px;background:linear-gradient(90deg,#2a2420,#4a3a32 40%,#3a2e2a 65%,#2a2320)}
.appoint-quote{top:1128px;font-size:21px;line-height:32px;color:var(--blue);letter-spacing:1px}
.appoint-cta{top:1208px;font-size:23px;font-weight:600;color:var(--white)}
.btn-outline{border:2px solid var(--white);border-radius:32px;color:var(--white);display:flex;align-items:center;justify-content:center;font-size:18px;font-weight:500}
.book{left:494px;top:1276px;width:212px;height:61px}

/* serve */
.serve-title{top:1428px;font-size:42px;color:var(--blue);letter-spacing:2px}
.card{top:1521px;width:312px;height:386px;border:2px solid #ddd;background:#f4f4f4}
.card-head{position:absolute;left:-2px;top:-2px;width:312px;height:158px;clip-path:polygon(0 0,100% 0,100% 75%,50% 100%,0 75%);text-align:center;color:var(--white)}
.card.blue .card-head{background:var(--blue)}
.card.grey .card-head{background:var(--grey)}
.card-name{font-size:21px;font-weight:600;margin-top:20px}
.card-price{font-size:19px;font-weight:600;margin-top:6px}
.card-shop{display:inline-block;margin-top:10px;background:var(--white);color:#333;font-size:16px;font-weight:500;padding:11px 18px}
.card-product{position:absolute;left:106px;top:166px;width:96px;height:208px;border-radius:14px}
.best{left:150px;top:1907px;width:166px;height:40px;background:var(--blue);color:var(--white);font-size:13px;font-weight:500;display:flex;align-items:center;justify-content:center}

/* career */
.career{top:2001px;left:0;width:1200px;height:458px;background:linear-gradient(180deg,#5aa6d6,#4b93c8 60%,#3f86bd)}
.career-title{top:2045px;font-size:42px;color:#223;letter-spacing:1px}
.info{left:260px;top:2124px}
.career-text{left:327px;top:2121px;width:630px;font-size:14.5px;line-height:26px;color:var(--white)}
.field{border:1.5px solid rgba(255,255,255,.85);color:var(--white);font-size:13.5px;padding:7px 9px;background:rgba(255,255,255,.05)}
.f-name{left:312px;top:2200px;width:285px;height:36px}
.f-mail{left:605px;top:2200px;width:285px;height:36px}
.f-msg{left:312px;top:2244px;width:578px;height:101px}
.submit{left:496px;top:2356px;width:206px;height:48px;font-size:16px;font-weight:600}

/* franchise */
.fr-title{top:2494px;font-size:42px;color:var(--blue);letter-spacing:1px}
.fr-sub{top:2558px;font-size:14px;font-weight:500;color:#333;letter-spacing:1px}
.loc{top:2608px;display:flex;gap:22px}
.loc p{width:240px;font-size:14px;line-height:22px;color:#444}
.map{top:2714px;left:0;width:1200px;height:291px;background:linear-gradient(90deg,#e8e4dc,#ece8e0 60%,#ddd9cf 88%,#a8c4e0)}

/* footer */
.footer{top:3005px;left:0;width:1200px;height:158px;background:var(--footer)}
.social{top:3043px;left:483px;display:flex;gap:17px}
.social span{width:46px;height:46px;border-radius:50%;border:2px solid var(--white)}
.social span:first-child{background:var(--blue);border-color:var(--blue)}
.copy{top:3114px;font-size:14px;color:var(--white);letter-spacing:1px}
.copy b{color:var(--blue);font-weight:400}
</style>
</head>
<body>

<header>
  <div class="abs brand">
    <span class="brand-dot"></span>
    <div>
      <div class="brand-name">VornaDerm</div>
      <div class="brand-tag">THE EXPERTS IN PERMANENT HAIR REMOVAL</div>
    </div>
  </div>
  <nav class="abs nav">
    <a class="active">Home</a><a>About</a><a>Studios</a><a>Appoinment</a><a>Carrers</a><a>Feanchise</a><a>Contact Us</a>
  </nav>
</header>

<section>
  <div class="abs hero"></div>
  <div class="abs hero-man" role="img" aria-label="Photo of a man with smooth bare chest"></div>
  <div class="abs hero-woman" role="img" aria-label="Photo of a woman in a white towel showing smooth legs"></div>
  <div class="abs hero-copy">
    <div class="hero-kicker serif">WE ARE SPECIALIZED ON</div>
    <div class="hero-title">Permantent Hair Removal</div>
    <div class="hero-sub serif">FOR THE BODY FOR MEN AND WOMAN</div>
  </div>
  <div class="abs dots"><span></span><span></span><span></span></div>
</section>

<section>
  <div class="abs why"></div>
  <div class="abs why-mark"></div>
  <h2 class="abs full why-title serif">Why Permanent Epilation</h2>
  <p class="abs why-text">Lorem ipsum dolor sit amet, consectetur adipiscing elit, sed do eiusmod tempor incididunt ut labore et dolore magna aliqua. Ut enim ad minim veniam, quis nostrud exercitation ullamco laboris nisi ut aliquip ex ea commodo consequat.</p>
</section>

<section>
  <div class="abs appoint" role="img" aria-label="Dark photo of smiling women in sunglasses"></div>
  <p class="abs full appoint-quote serif">People should trust in us. We take care about their<br>body. This need to be communicated 100%.</p>
  <p class="abs full appoint-cta">Book your Appointment</p>
  <div class="abs btn-outline book">Book Now</div>
</section>

<section>
  <h2 class="abs full serve-title serif">What We Searve</h2>
  <div class="abs card blue" style="left:78px">
    <div class="card-head"><div class="card-name">LOREM IPSUME</div><div class="card-price">$66.18</div><div class="card-shop">Shop Now</div></div>
    <div class="card-product" role="img" aria-label="Purple hair removal cream bottle" style="background:linear-gradient(180deg,#e8c8dc,#8a1f5c)"></div>
  </div>
  <div class="abs best">BEST OFFERS</div>
  <div class="abs card grey" style="left:443px">
    <div class="card-head"><div class="card-name">LOREM IPSUME</div><div class="card-price">$66.18</div><div class="card-shop">Shop Now</div></div>
    <div class="card-product" role="img" aria-label="Green and white shave gel tube" style="background:linear-gradient(180deg,#fff,#e8e8e8 45%,#4fb04a 60%,#3f9a3c 80%,#888)"></div>
  </div>
  <div class="abs card grey" style="left:810px">
    <div class="card-head"><div class="card-name">LOREM IPSUME</div><div class="card-price">$66.18</div><div class="card-shop">Shop Now</div></div>
    <div class="card-product" role="img" aria-label="Hair removal cream tube" style="background:linear-gradient(180deg,#eee,#d8a070 55%,#2d3b70)"></div>
  </div>
</section>

<section>
  <div class="abs career" role="img" aria-label="Blue tinted city skyline photo"></div>
  <h2 class="abs full career-title serif">Creer With Us</h2>
  <svg class="abs info" width="50" height="50" viewBox="0 0 50 50" aria-hidden="true">
    <circle cx="25" cy="25" r="22" fill="none" stroke="#fff" stroke-width="3"/>
    <circle cx="25" cy="14" r="3" fill="#fff"/>
    <rect x="22" y="21" width="6" height="17" fill="#fff"/>
  </svg>
  <p class="abs career-text">Lorem ipsum dolor sit amet, consectetur adipiscing elit, sed do eiusmod tempor incididunt ut labore et dolore magna aliqua. Ut enim ad minim veniam, quis nostrud.</p>
  <div class="abs field f-name">Name</div>
  <div class="abs field f-mail">Email Id</div>
  <div class="abs field f-msg">Message</div>
  <div class="abs btn-outline submit">SUBMIT</div>
</section>

<section>
  <h2 class="abs full fr-title serif">Our Franchise</h2>
  <p class="abs full fr-sub serif">NEW AVAILABLE LOCATIONS FOLLOW</p>
  <div class="abs loc" style="left:74px">
    <svg width="24" height="32" viewBox="0 0 24 32" aria-hidden="true"><path d="M12 1C6 1 1 6 1 12c0 8 11 19 11 19s11-11 11-19C23 6 18 1 12 1z" fill="var(--blue)"/><circle cx="12" cy="12" r="4.5" fill="#fff"/></svg>
    <p>Lorem ipsum dolor sit amet, consectetur adipiscing elit, sed do eiusmod tempor.</p>
  </div>
  <div class="abs loc" style="left:454px">
    <svg width="24" height="32" viewBox="0 0 24 32" aria-hidden="true"><path d="M12 1C6 1 1 6 1 12c0 8 11 19 11 19s11-11 11-19C23 6 18 1 12 1z" fill="var(--blue)"/><circle cx="12" cy="12" r="4.5" fill="#fff"/></svg>
    <p>Lorem ipsum dolor sit amet, consectetur adipiscing elit, sed do eiusmod tempor.</p>
  </div>
  <div class="abs loc" style="left:853px">
    <svg width="24" height="32" viewBox="0 0 24 32" aria-hidden="true"><path d="M12 1C6 1 1 6 1 12c0 8 11 19 11 19s11-11 11-19C23 6 18 1 12 1z" fill="var(--blue)"/><circle cx="12" cy="12" r="4.5" fill="#fff"/></svg>
    <p>Lorem ipsum dolor sit amet, consectetur adipiscing elit, sed do eiusmod tempor.</p>
  </div>
  <div class="abs map" role="img" aria-label="Street map of the franchise locations"></div>
</section>

<footer>
  <div class="abs footer"></div>
  <div class="abs social" aria-label="Social links"><span></span><span></span><span></span><span></span></div>
  <p class="abs full copy serif">© <b>VornaDerm</b> - All Rights Reserved.</p>
</footer>

</body>
</html>
```